Business Card Design

Lintel Comms is a public relations consultancy service for the self build, home refurbishment and home improvement market.
It represents everything about 'home' so envisage logo featuring maybe roof pitch over the 'A' of Lintel. Colour/font undecided.

Industry/Entity Type

Home Improvement

Contact Information for Business Card

Fenella Coxworth
fenella@lintelcomms.co.uk
Telephone Direct: 0788 142 6597

```html
<!DOCTYPE html>
<html lang="en">
<head>
<meta charset="utf-8">
<title>Lintel Comms – Business Card</title>
<link rel="stylesheet" href="https://fonts.googleapis.com/css2?family=Arimo:wght@400;700&display=swap">
<style>
  :root {
    --page-bg: #e9ebee;
    --card-black: #050505;
    --card-black-soft: #1c1c1c;
    --band-blue-light: #5cc8ef;
    --band-blue: #2a9fe0;
    --band-blue-deep: #1572c4;
    --divider: #ffffff;
    --text-light: #ffffff;
  }
  html, body {
    margin: 0;
    width: 1200px;
    height: 855px;
    overflow: hidden;
    background: var(--page-bg);
    font-family: "Arimo", Arial, sans-serif;
  }
  .business-card {
    position: absolute;
    left: 180px;
    top: 187px;
    width: 840px;
    height: 480px;
    border-radius: 30px;
    overflow: hidden;
    background: linear-gradient(160deg, var(--card-black-soft) 0%, var(--card-black) 45%);
    box-shadow: 0 10px 30px rgba(0,0,0,0.18);
  }
  .divider-stripe {
    position: absolute;
    inset: 0;
    background: var(--divider);
    clip-path: polygon(59% 0, 100% 0, 100% 100%, 44% 100%);
  }
  .contact-band {
    position: absolute;
    inset: 0;
    background: linear-gradient(200deg, var(--band-blue-deep) 0%, var(--band-blue) 45%, var(--band-blue-light) 100%);
    clip-path: polygon(60.2% 0, 100% 0, 100% 100%, 45.2% 100%);
  }
  .brand {
    position: absolute;
    left: 64px;
    top: 160px;
    display: flex;
    align-items: center;
    gap: 16px;
  }
  .brand-mark {
    width: 26px;
    height: 26px;
    background: var(--text-light);
    flex: none;
  }
  .brand-name {
    font-weight: 700;
    font-size: 56px;
    line-height: 1.05;
    letter-spacing: 1px;
    color: var(--text-light);
    text-transform: uppercase;
  }
  .brand-name span {
    display: block;
  }
  .contact-block {
    position: absolute;
    left: 510px;
    top: 150px;
    color: var(--text-light);
  }
  .person-name {
    font-weight: 700;
    font-size: 34px;
    margin: 0 0 34px;
  }
  .contact-line {
    display: flex;
    align-items: center;
    gap: 12px;
    font-size: 22px;
    margin-bottom: 14px;
  }
  .contact-icon {
    width: 22px;
    height: 22px;
    flex: none;
  }
</style>
</head>
<body>
  <div class="business-card">
    <div class="divider-stripe"></div>
    <div class="contact-band"></div>

    <div class="brand">
      <span class="brand-mark"></span>
      <span class="brand-name"><span>Lintel</span><span>Comms</span></span>
    </div>

    <div class="contact-block">
      <p class="person-name">Fenella Coxworth</p>
      <div class="contact-line">
        <svg class="contact-icon" viewBox="0 0 22 22" aria-hidden="true">
          <circle cx="11" cy="11" r="10.5" fill="#ffffff"/>
          <rect x="7.5" y="4.5" width="7" height="13" rx="1.2" fill="none" stroke="#1f86d0" stroke-width="1.6"/>
          <circle cx="11" cy="15" r="0.9" fill="#1f86d0"/>
        </svg>
        <span>0788 142 6597</span>
      </div>
      <div class="contact-line">
        <svg class="contact-icon" viewBox="0 0 22 22" aria-hidden="true">
          <circle cx="11" cy="11" r="10.5" fill="#ffffff"/>
          <rect x="5" y="7" width="12" height="8.5" rx="1" fill="none" stroke="#1f86d0" stroke-width="1.6"/>
          <polyline points="5.5,7.5 11,12 16.5,7.5" fill="none" stroke="#1f86d0" stroke-width="1.6"/>
        </svg>
        <span>fenella@lintelcomms.co.uk</span>
      </div>
    </div>
  </div>
</body>
</html>
```